Website Design Requirements

Domain Name: HometownTradesfolkRegistry.com

Website Look: Simple, Clean, Modern, and Professional Awarding Winning Website. Our Platform is the Best Directory Platform, all we need is a very creative person to make the following designs and select the fonts, font sizing, font colors and all the colors for the color points. We will follow up with the winner of the contest to design the rest of our design needs. The highlight of our brand is our Mascot; we feel this is something everyone will remember. It may be the easiest to obtain a free trial of the platform from Vantory Listings to complete this project. When we pick a winner of this contest we will provide the password to our admin panel for everything to be applied. Our Competitors are Perrows Hub, Yardwise Pro and Gravelnook.

We are thinking a light gray scale shadowing or graduated ghosting for the background behind the image of the Mascot for the main image. We want the Mascot and the Selection box to stand out as well as the logo.

Design Elements:
Main Page Image-Size for website is 1800 X 600px should be the Mascot on the right half of the image; this is where creative design is the most important. Design can use the head only from the waist up or the full image

Logo- Size for website is 450 X 70px; the logo should have the head of the mascot on a 3D icon with 2 line of text to the right side. The top line should have Hometown Tradesfolk the second line should have the word Directory in smaller size and be ghosted. The main idea about the logo is the icon and the words Hometown Tradesfolk. Note example can be seen on the Vantory Listings Rapid Launch Walkthrough on Clip Vue.

Favicon- Size for website is 56 X 56px should be the head of the mascot the Favicon and Google Map Pin drop could be the same if design is nice enough

Google Map Pin Drop- 25 X 46px should be the head of the mascot with a arrow pointing down.

Member Badge Image- Size 250 X 250px should be the head of the mascot inside a round ring with the words Verified –Certified –Member.

Target Market(s)

Consumers will use this website to locate Contractors in their Local area. Contractors will list their business on this website for a fee.

Industry/Entity Type

Domain

Contact Information for Business Card

Marcus Oldfield
Partner
555.014.2871
Marcus@HometownTradesfolkRegistry.Com
WWW. HometownTradesfolkRegistry.com

Logo Text

Hometown Tradesfolk Registry

Number of Pages Required

3 page

Font styles to use
Serif

Colors
ec1f27
fbed22

Requirements
Must have
• The use of our mascot, you can use full body view, waist up or head shot
Nice to have
• Clean bright colored Mascot, listing on back of card
• Hometown Tradesfolk
• Electricians
• Plumbers
• HVAC
• Landscapers
• General Contractors
• Garage Door Repair
• Carpet Cleaners
• Concrete Contractors

```html
<!DOCTYPE html>
<html lang="en">
<head>
<meta charset="utf-8">
<title>Find Top-Rated Contractor</title>
<link rel="stylesheet" href="https://fonts.googleapis.com/css2?family=Arimo:wght@400&display=swap">
<style>
  :root {
    --title-brown: #4a1e06;
    --button-brown: #461a02;
    --panel-red-top: rgba(226, 40, 44, 0.86);
    --panel-red-bottom: rgba(255, 96, 96, 0.82);
    --panel-border: #6b5a52;
    --field-white: #ffffff;
    --field-border: #5a2410;
    --label-white: #ffffff;
    --backdrop-light: #d6d0ca;
    --backdrop-mid: #b9afa6;
    --backdrop-dark: #9c8f84;
    --mascot-yellow: #f5c21b;
    --mascot-red: #d8262c;
    --mascot-skin: #f2b27e;
  }
  * { box-sizing: border-box; margin: 0; padding: 0; }
  html, body {
    width: 1200px;
    height: 400px;
    overflow: hidden;
    background: #ffffff;
  }
  .hero {
    position: relative;
    width: 1200px;
    height: 400px;
    overflow: hidden;
    font-family: "Arimo", Arial, sans-serif;
  }
  .hero-backdrop {
    position: absolute;
    inset: 0;
    background:
      radial-gradient(ellipse at 70% 35%, rgba(120, 104, 92, 0.35), transparent 60%),
      linear-gradient(90deg, var(--backdrop-light) 0%, var(--backdrop-mid) 45%, var(--backdrop-dark) 100%);
  }
  .mascot {
    position: absolute;
    left: 880px;
    top: 6px;
    width: 256px;
    height: 394px;
    border-radius: 110px 110px 24px 24px;
    background: linear-gradient(180deg, var(--mascot-yellow) 0%, var(--mascot-yellow) 22%, var(--mascot-skin) 22%, var(--mascot-skin) 56%, var(--mascot-red) 56%, var(--mascot-red) 100%);
  }
  .headline {
    position: absolute;
    left: 27px;
    top: 38px;
    color: var(--title-brown);
    font-size: 58px;
    font-weight: 400;
    line-height: 62px;
    letter-spacing: 0;
  }
  .search-panel {
    position: absolute;
    left: 22px;
    top: 178px;
    width: 632px;
    height: 162px;
    border: 1.5px solid var(--panel-border);
    border-radius: 7px;
    background: linear-gradient(180deg, var(--panel-red-top), var(--panel-red-bottom));
  }
  .search-row {
    position: absolute;
    left: 0;
    display: flex;
    align-items: center;
    height: 37px;
  }
  .search-row--need { top: 12px; }
  .search-row--place { top: 62px; }
  .search-label {
    width: 256px;
    padding-right: 8px;
    text-align: right;
    color: var(--label-white);
    font-size: 22px;
  }
  .search-field {
    width: 346px;
    height: 37px;
    border: 1.5px solid var(--field-border);
    border-radius: 6px;
    background: var(--field-white);
    font: inherit;
    font-size: 18px;
    padding: 0 10px;
  }
  .search-button {
    position: absolute;
    left: 265px;
    top: 111px;
    width: 346px;
    height: 37px;
    border: none;
    border-radius: 5px;
    background: var(--button-brown);
    color: var(--label-white);
    font-family: inherit;
    font-size: 21px;
  }
</style>
</head>
<body>
  <main class="hero">
    <div class="hero-backdrop" role="img" aria-label="Faded photograph of hand tools — axes, hammers, pliers and work gloves — on weathered wooden planks"></div>

    <h1 class="headline">Find Top-Rated<br>Contractor !</h1>

    <form class="search-panel" action="#">
      <div class="search-row search-row--need">
        <label class="search-label" for="need">What do you need?</label>
        <input class="search-field" id="need" type="text">
      </div>
      <div class="search-row search-row--place">
        <label class="search-label" for="place">Located in:</label>
        <input class="search-field" id="place" type="text">
      </div>
      <button class="search-button" type="submit">Search Now</button>
    </form>

    <div class="mascot" role="img" aria-label="Cartoon contractor mascot in a yellow hard hat and red shirt, smiling with arms crossed, shown from the waist up"></div>
  </main>
</body>
</html>
```